Levy Compass Capability Statement

Need a fold-out flyer (A5 size) that outlines my yacht-related capabilities for handing out at a trade show. Something similar to the attached and based on my website www.levycompass-example.com.

Target Market(s)

Superyacht owners and managers

Industry/Entity Type

Professional services

Colors
0054AA
0677BA
7BADD7
CADEEF
E8F1F8

Requirements
Must have
• Impact and a clear message about value proposition
Nice to have
• Spectacular images
Should not have
• Too many words

```html
<!DOCTYPE html>
<html lang="en">
<head>
<meta charset="utf-8">
<title>Levy Compass – Capability Statement</title>
<link rel="stylesheet" href="https://fonts.googleapis.com/css2?family=Poppins:wght@400;500;700;800&display=swap">
<style>
  :root {
    --navy: #1f2a5a;
    --accent: #6a96d2;
    --accent-soft: #cadeef;
    --paper: #ffffff;
    --ink: #1a1a1a;
    --sea-top: #2f8fe0;
    --sea-bottom: #6fd6d6;
  }
  * { margin: 0; padding: 0; box-sizing: border-box; }
  html, body { width: 1200px; height: 424px; overflow: hidden; background: var(--paper); }
  body { font-family: "Poppins", sans-serif; color: var(--ink); }

  .flyer { position: relative; width: 1200px; height: 424px; overflow: hidden; background: var(--paper); }
  .backdrop { position: absolute; inset: 0; }

  .page-fold {
    position: absolute; left: 585px; top: 0; width: 40px; height: 424px;
    background: linear-gradient(90deg, rgba(0,0,0,0) 0%, rgba(0,0,0,0.06) 60%, rgba(0,0,0,0) 100%);
  }

  /* Cover panel */
  .cover-copy { position: absolute; left: 31px; top: 64px; width: 250px; color: #fff; }
  .cover-title { font-weight: 800; font-size: 16.6px; line-height: 20.5px; letter-spacing: -0.1px; white-space: nowrap; }
  .cover-title span { color: var(--accent); display: block; }
  .cover-text { margin-top: 14px; font-size: 11px; line-height: 12.1px; font-weight: 400; }
  .cover-text + .cover-text { margin-top: 12px; }
  .promise-list { list-style: none; margin-top: 5px; font-size: 11px; line-height: 12.1px; }
  .promise-list li { position: relative; padding-left: 9px; }
  .promise-list li::before {
    content: ""; position: absolute; left: 0; top: 4px; width: 5px; height: 5px;
    border-radius: 50%; background: var(--accent);
  }

  .hero-photo {
    position: absolute; left: 338px; top: 94px; width: 231px; height: 191px;
    background: linear-gradient(180deg, var(--sea-top) 0%, #8cc4ef 45%, var(--sea-bottom) 70%, #bfeee8 100%);
    box-shadow: 0 10px 12px -6px rgba(0,0,0,0.35);
  }

  .brand-name {
    position: absolute; font-family: "Poppins", sans-serif; font-weight: 700;
    font-size: 13px; letter-spacing: 1.6px; white-space: nowrap;
  }
  .brand-name--cover { left: 31px; top: 372px; color: #fff; }
  .brand-name--inside { left: 630px; top: 372px; color: var(--navy); }

  .web-tag { position: absolute; top: 371px; height: 23px; display: flex; }
  .web-tag__url {
    height: 23px; background: var(--navy); color: #fff; font-weight: 700; font-size: 10px;
    line-height: 23px; padding: 0 10px 0 13px; white-space: nowrap;
    clip-path: polygon(5px 0, 100% 0, calc(100% - 5px) 100%, 0 100%);
  }
  .web-tag__page {
    height: 23px; width: 25px; margin-left: 2px; background: var(--accent); color: #fff;
    font-weight: 700; font-size: 11px; line-height: 23px; text-align: center; padding-left: 3px;
    clip-path: polygon(5px 0, 100% 0, 100% 100%, 0 100%);
  }
  .web-tag--cover { right: 631px; }
  .web-tag--inside { right: 31px; }

  /* Inside panel */
  .world-texture {
    position: absolute; left: 800px; top: 280px; width: 400px; height: 144px;
    background: radial-gradient(ellipse at 55% 70%, rgba(202,222,239,0.55) 0%, rgba(232,241,248,0.3) 50%, rgba(255,255,255,0) 75%);
  }
  .solutions-title {
    position: absolute; left: 630px; top: 73px; font-weight: 800; font-size: 16.9px;
    letter-spacing: -0.1px; color: #111; white-space: nowrap;
  }
  .solutions-title span { color: var(--accent); }

  .service { position: absolute; width: 212px; }
  .service__icon {
    position: absolute; left: -45px; top: -4px; width: 36px; height: 36px; border-radius: 50%;
    background: #fff; box-shadow: -3px 3px 6px rgba(0,0,0,0.12);
    display: flex; align-items: center; justify-content: center;
  }
  .service__title { font-weight: 800; font-size: 11.8px; line-height: 14px; color: #111; letter-spacing: 0.1px; white-space: nowrap; }
  .service__text { margin-top: 1px; font-size: 11px; line-height: 12.1px; color: #111; }
  .service--gst { left: 676px; top: 122px; }
  .service--regulatory { left: 967px; top: 122px; width: 204px; }
  .service--charter { left: 676px; top: 199px; }
  .service--marine { left: 967px; top: 199px; width: 204px; }
</style>
</head>
<body>
<main class="flyer">
  <svg class="backdrop" width="1200" height="424" viewBox="0 0 1200 424" aria-hidden="true">
    <polygon points="0,0 527,0 238,424 0,424" fill="var(--navy)"/>
    <polygon points="536,0 587,0 298,424 247,424" fill="var(--accent)"/>
  </svg>
  <div class="page-fold" aria-hidden="true"></div>

  <section class="cover">
    <div class="cover-copy">
      <h1 class="cover-title">NAVIGATE AUSTRALIA'S TAX <span>WATERS WITH CONFIDENCE</span></h1>
      <p class="cover-text">With over 25 years mastering Australian GST law, Levy Compass delivers end-to-end support for foreign-flagged superyachts entering for private use or commercial charters.</p>
      <p class="cover-text">We handle the complexities from registrations and ownership structures to ATO representation, so you focus on exceptional experiences in world-class destinations.</p>
      <p class="cover-text">Our proactive approach ensures:</p>
      <ul class="promise-list">
        <li>Seamless Compliance</li>
        <li>Tax Efficiency</li>
        <li>Zero Surprises.</li>
      </ul>
    </div>
    <div class="hero-photo" role="img" aria-label="Photo of a white motor yacht anchored in clear turquoise shallows under a blue sky"></div>
    <div class="brand-name brand-name--cover">LEVY COMPASS</div>
    <div class="web-tag web-tag--cover">
      <span class="web-tag__url">www.levycompass-example.com</span>
      <span class="web-tag__page">1</span>
    </div>
  </section>

  <section class="inside">
    <div class="world-texture" role="img" aria-label="Faint dotted world map decoration"></div>
    <h2 class="solutions-title">TAILORED YACHT <span>TAX SOLUTIONS</span></h2>

    <article class="service service--gst">
      <div class="service__icon">
        <svg width="20" height="20" viewBox="0 0 20 20" aria-hidden="true">
          <rect x="7" y="3" width="6" height="4" fill="var(--navy)"/>
          <path d="M4 8h12v4l-2 4H6l-2-4z" fill="var(--navy)"/>
          <path d="M2 17.5q2-1.5 4 0t4 0 4 0 4 0" stroke="var(--accent)" stroke-width="1.2" fill="none"/>
        </svg>
      </div>
      <h3 class="service__title">GST RECOVERY &amp; COMPLIANCE</h3>
      <p class="service__text">Secure full credits on fuel, maintenance, and local spend; expert advice on classification and attribution</p>
    </article>

    <article class="service service--regulatory">
      <div class="service__icon">
        <svg width="20" height="20" viewBox="0 0 20 20" aria-hidden="true">
          <circle cx="10" cy="10" r="7" fill="var(--navy)"/>
          <text x="10" y="13.5" text-anchor="middle" font-family="Poppins, sans-serif" font-size="10" font-weight="700" fill="#fff">$</text>
        </svg>
      </div>
      <h3 class="service__title">REGULATORY REPRESENTATION</h3>
      <p class="service__text">Fiscal agency for non-residents; we manage ATO dealings, private rulings, and audits on your behalf</p>
    </article>

    <article class="service service--charter">
      <div class="service__icon">
        <svg width="20" height="20" viewBox="0 0 20 20" aria-hidden="true">
          <rect x="3" y="3" width="7" height="10" rx="1" fill="var(--accent)"/>
          <rect x="8" y="4" width="9" height="13" rx="1" fill="var(--navy)"/>
          <path d="M10 7h5M10 10h5M10 13h5" stroke="#fff" stroke-width="1"/>
        </svg>
      </div>
      <h3 class="service__title">CHARTER STRUCTURING</h3>
      <p class="service__text">Tax-effective setups for commercial operations, minimizing risks and aligning with ATO standards</p>
    </article>

    <article class="service service--marine">
      <div class="service__icon">
        <svg width="20" height="20" viewBox="0 0 20 20" aria-hidden="true">
          <rect x="4" y="3" width="10" height="14" rx="1" fill="var(--navy)"/>
          <path d="M6 7l1 1 2-2M6 11l1 1 2-2M10 7h2M10 11h2" stroke="#fff" stroke-width="1" fill="none"/>
          <circle cx="15" cy="13" r="3.5" fill="var(--accent)"/>
        </svg>
      </div>
      <h3 class="service__title">MARINE SECTOR EXPERTISE</h3>
      <p class="service__text">Ownership planning, stakeholder support, and training to keep your operations compliant and optimized</p>
    </article>

    <div class="brand-name brand-name--inside">LEVY COMPASS</div>
    <div class="web-tag web-tag--inside">
      <span class="web-tag__url">www.levycompass-example.com</span>
      <span class="web-tag__page">2</span>
    </div>
  </section>
</main>
</body>
</html>
```